Algae Cream Package Concept

Creative Brief — Solvane: Phytoplankton Rescue Cream (100 ml)
Product Snapshot
Name: Solvane: Phytoplankton Rescue Cream
Format: 100 ml / 3.4 fl oz tube or airless pump (dieline provided)
Dieline attached:
Purpose & Key Benefits
Rescue dry or damaged skin—especially eczema & psoriasis.
All‑over use: hands, feet, elbows, knees, face, body.
Repairs barrier · Deep hydration · Calms irritation · Antioxidant shield.
Usage
Longevity: ~30 days when used daily on 10 in² of skin.
How: Apply pea‑size to clean, damp skin; massage ≥1 min; reapply as needed.
Ingredients
Label Ingredients:
Aloe Barbadensis (Aloe) Leaf Juice, Butyrospermum Parkii (Shea) Butter, Aqua (and) Propanediol (and) Nannochloropsis Gaditana (Phytoplankton) Extract, Simmondsia Chinensis (Jojoba) Seed Oil, Sodium Lactate, Cetyl Alcohol, Cetearyl Olivate (and) Sorbitan Olivate (Tesaril 400), Panthenol (Vitamin B5), Gluconolactone (and) Sodium
Benzoate (and) Calcium Gluconate (Corvex Prime), Illite (French Green Clay).
Look & Feel (for designer)
Minimal, ocean‑inspired, premium yet approachable. Off‑white base, deep‑teal accent, subtle algae texture.
Must‑Haves on Pack
Product name + “Rescue Cream” descriptor
Net weight (100 ml / 3.4 fl oz)
Tagline: “Reunite your skin with Earth’s base nutrition.”
Copy snippet: “Powered by sustainably grown phytoplankton.”
Icons: Vegan • Cruelty‑Free • Reef‑Safe • Recyclable
www.brimtidelabs.com

```html
<!DOCTYPE html>
<html lang="en">
<head>
<meta charset="utf-8">
<title>Solvane: Phytoplankton Rescue Cream — Label Set</title>
<link href="https://fonts.googleapis.com/css2?family=Cormorant+Garamond:ital,wght@0,400;0,500;0,600;1,400&family=Cormorant+SC:wght@500&display=swap" rel="stylesheet">
<style>
  :root {
    --page: #ffffff;
    --teal-band: #4f9f9f;
    --teal-deep: #1f5e66;
    --teal-ink: #2f7a80;
    --panel: rgba(214, 236, 234, 0.93);
    --wash-light: #e9f6f8;
    --wash-mid: #9fd3dc;
    --wash-deep: #3fa7b8;
    --band-text: #f3fbfb;
    --badge-fill: #eaf5f5;
    --badge-ring: #9cc9c8;
  }
  * { box-sizing: border-box; margin: 0; padding: 0; }
  html, body { width: 1200px; height: 1200px; overflow: hidden; }
  body {
    background: var(--page);
    font-family: "Cormorant Garamond", Georgia, serif;
    position: relative;
  }
  .label {
    position: absolute;
    top: 310px;
    width: 540px;
    height: 580px;
    border-radius: 10px;
    overflow: hidden;
  }
  .label--front { left: 30px; }
  .label--back { left: 630px; }
  .label__texture {
    position: absolute; inset: 0;
    background:
      radial-gradient(ellipse 70% 30% at 75% 25%, var(--wash-deep) 0%, transparent 70%),
      radial-gradient(ellipse 50% 40% at 10% 55%, var(--wash-mid) 0%, transparent 75%),
      radial-gradient(ellipse 80% 35% at 60% 85%, var(--wash-mid) 0%, transparent 70%),
      linear-gradient(170deg, var(--wash-light) 0%, #c4e7ec 40%, #8ccbd6 60%, #cfeef2 100%);
  }
  .panel {
    position: absolute;
    left: 100px;
    top: 142px;
    width: 340px;
    display: flex;
    flex-direction: column;
  }
  .label--back .panel { top: 150px; }
  .band {
    background: var(--teal-band);
    color: var(--band-text);
    padding: 0 20px;
    display: flex;
    align-items: center;
  }
  .band--top {
    height: 38px;
    font-style: italic;
    font-size: 15px;
  }
  .band--bottom {
    height: 40px;
    font-size: 15px;
  }
  .panel__body {
    background: var(--panel);
    position: relative;
    padding: 14px 20px 10px;
  }
  .botanical-wash {
    position: absolute;
    right: 12px; bottom: 0;
    width: 200px; height: 150px;
    background: radial-gradient(ellipse at 55% 60%, rgba(140,190,186,0.35) 0%, transparent 70%);
  }
  .product-name {
    font-family: "Cormorant SC", "Cormorant Garamond", serif;
    font-weight: 500;
    font-size: 40px;
    line-height: 1;
    color: var(--teal-deep);
    letter-spacing: 0.5px;
  }
  .descriptor {
    font-size: 20px;
    color: var(--teal-deep);
    line-height: 1.2;
    margin-top: 2px;
  }
  .brand-mark {
    display: flex;
    align-items: center;
    gap: 10px;
    margin: 14px 0 14px 6px;
    position: relative;
    height: 66px;
  }
  .brand-mark__circle {
    width: 20px; height: 20px;
    border-radius: 50%;
    background: var(--teal-ink);
    flex: none;
  }
  .brand-mark__name {
    font-size: 15px;
    font-weight: 400;
    color: var(--teal-ink);
  }
  .benefits {
    font-size: 14px;
    color: var(--teal-deep);
    line-height: 1.3;
    position: relative;
  }
  .info { position: relative; font-size: 8.6px; line-height: 1.55; color: var(--teal-ink); }
  .info p { margin-bottom: 4px; }
  .info strong { font-weight: 600; color: var(--teal-deep); }
  .info .ingredients-head { margin-top: 10px; }
  .info .ingredients { font-size: 8.4px; line-height: 1.85; }
  .band--icons { height: 42px; justify-content: center; gap: 26px; }
  .cert-badge {
    width: 24px; height: 24px;
    border-radius: 50%;
    background: var(--badge-fill);
    border: 2px solid var(--badge-ring);
  }
</style>
</head>
<body>

<section class="label label--front">
  <div class="label__texture" role="img" aria-label="Soft blue-teal watercolour algae texture background"></div>
  <div class="panel">
    <div class="band band--top">Powered by sustainably grown Phytoplankton</div>
    <div class="panel__body">
      <div class="botanical-wash" role="img" aria-label="Faint line illustration of seaweed and marine plants"></div>
      <h1 class="product-name">Solvane</h1>
      <p class="descriptor">Phytoplankton Rescue Cream</p>
      <div class="brand-mark">
        <span class="brand-mark__circle"></span>
        <span class="brand-mark__name">Solvane</span>
      </div>
      <p class="benefits">Repairs Barrier &nbsp;•&nbsp; Deep Hydration<br>Calms Irritation &nbsp;•&nbsp; Antioxidant Shield</p>
    </div>
    <div class="band band--bottom">Net weight (100 ml / 3.4 floz)</div>
  </div>
</section>

<section class="label label--back">
  <div class="label__texture" role="img" aria-label="Soft blue-teal watercolour algae texture background"></div>
  <div class="panel">
    <div class="band band--top">Powered by sustainably grown Phytoplankton</div>
    <div class="panel__body">
      <div class="botanical-wash" role="img" aria-label="Faint line illustration of seaweed and marine plants"></div>
      <div class="info">
        <p><strong>Uses:</strong> Rescue dry or damaged skin - especially Eczema &amp; Psoriasis.</p>
        <p><strong>Longevity:</strong> ~30 days when used daily on skin.</p>
        <p><strong>How:</strong> Apply pea-size to clean, damp skin and massage. Reapply as needed</p>
        <p><strong>All-over use:</strong> Hands, feet, elbows, knees, face and body.</p>
        <p class="ingredients-head"><strong>Ingredients:</strong></p>
        <p class="ingredients">Aloe Barbadensis (<em>Aloe</em>) Leaf Juice, Butyrospermum Parkii (<em>Shea</em>) Butter, Aqua (and) Propanediol (and) Nannochloropsis Gaditana (<em>Phytoplankton</em>) Extract, Simmondsia Chinensis (<em>Jojoba</em>) Seed Oil, Sodium Lactate, Cetyl Alcohol, Cetearyl Olivate (and) Sorbitan Olivate (<em>Tesaril 400</em>), Panthenol (<em>Vitamin B5</em>), Gluconolactone (and) Sodium Benzoate (and) Calcium Gluconate (<em>Corvex Prime</em>), Illite (<em>French Green Clay</em>).</p>
      </div>
    </div>
    <div class="band band--icons">
      <span class="cert-badge"></span>
      <span class="cert-badge"></span>
      <span class="cert-badge"></span>
      <span class="cert-badge"></span>
    </div>
  </div>
</section>

</body>
</html>
```